Maple Sprout Menu (Vegetarian Restaurant Concept)

Maple Sprout is a new concept fast casual restaurant
renders are attached so you can see the style of restaurant
Maple Sprowt is a vibrant and modern Vegetarian fast casual restaurant concept that mixes fresh food, energy, great décor, and a comfortable, welcoming atmosphere to provide a memorable and all Vegetarian dining experience.
Our Mission is to be top of mind when consumers think Vegetarian food!
Target Market(s)
the menu is vegetarian and appeals to a broad demographic in USA
Colors
Designer to choose colors to be used in the design.
Requirements
Must have
- well colored and well laid out menu - should not be cartoonish
Nice to have
- For Phots please use the shots in this file:
- https://www.filecrate-example.net/sh/kq7trm2wzl4pnad/BBBxT_qPwLdRNVoE_KMS_Tb?dl=0
- note these are untouched and you are free to change as needed
Should not have
- Should not be cartoonish - nor kives, forks etc in the design

```html
<!DOCTYPE html>
<html lang="en">
<head>
<meta charset="utf-8">
<title>Maple Sprowt Menu</title>
<link rel="stylesheet" href="https://fonts.googleapis.com/css2?family=Antonio:wght@300;400&family=Oswald:wght@300&family=Poppins:wght@400;500;600&display=swap">
<style>
  :root {
    --forest: #2f5529;
    --paper: #f1f1ef;
    --paper-shade: #e6e6e3;
    --orange: #e8742f;
    --bowl-orange: #f2a04f;
    --ink: #1d1d1b;
    --muted: #3c3c3a;
    --rule: #9a9a96;
    --white: #ffffff;
  }
  * { margin: 0; padding: 0; box-sizing: border-box; }
  html, body { width: 848px; height: 1200px; overflow: hidden; background: var(--forest); }
  .canvas {
    position: relative; width: 848px; height: 1200px; overflow: hidden;
    background: var(--forest);
    font-family: "Poppins", sans-serif; color: var(--ink);
  }
  .menu-card {
    position: absolute; left: 41px; top: 40px; width: 765px; height: 1120px;
    border-radius: 8px;
    background: linear-gradient(180deg, var(--paper) 0%, var(--paper-shade) 100%);
  }
  .brand {
    position: absolute; left: 229px; top: 80px; width: 100px;
    display: flex; flex-direction: column; align-items: center; gap: 10px;
  }
  .brand-dot { width: 34px; height: 34px; border-radius: 50%; background: var(--orange); }
  .brand-name {
    font-family: "Poppins", sans-serif; font-weight: 500; font-size: 14px;
    color: var(--forest); white-space: nowrap;
  }
  .menu-title {
    position: absolute; left: 347px; top: 84px;
    font-family: "Oswald", sans-serif; font-weight: 300; font-size: 48px;
    letter-spacing: 17px; color: var(--forest); line-height: 1;
  }
  .section-heading {
    font-family: "Antonio", sans-serif; font-weight: 300; font-size: 31px;
    color: var(--orange); text-transform: uppercase; line-height: 1;
    white-space: nowrap;
  }
  .column { position: absolute; text-align: center; }
  .column .section-heading { margin-bottom: 26px; }
  .salads { left: 76px; top: 208px; width: 352px; }
  .burgers { left: 436px; top: 208px; width: 350px; }
  .item { margin-bottom: 14px; }
  .item-name { font-weight: 500; font-size: 14.5px; line-height: 18px; }
  .item-desc { font-size: 10.5px; line-height: 13.5px; color: var(--muted); margin-top: 8px; }
  .burgers .item { margin-bottom: 16px; }
  .burgers .item.has-desc { margin-bottom: 24px; }
  .column-divider {
    position: absolute; left: 424px; top: 198px; width: 1px; height: 366px; background: var(--rule);
  }
  .rule { position: absolute; left: 76px; width: 694px; height: 1px; background: var(--rule); }
  .rule-top { top: 590px; }
  .rule-bottom { top: 764px; }
  .toasts-heading { position: absolute; left: 0; width: 848px; top: 620px; text-align: center; }
  .toast { position: absolute; top: 676px; text-align: center; }
  .toast .item-desc { margin-top: 10px; }
  .toast-a { left: 48px; width: 240px; }
  .toast-b { left: 304px; width: 240px; }
  .toast-c { left: 564px; width: 240px; }
  .bowls {
    position: absolute; left: 110px; top: 806px; width: 236px; height: 302px;
    border-radius: 10px; background: var(--bowl-orange); color: var(--white);
    text-align: center; padding-top: 32px;
  }
  .bowls .section-heading { color: var(--white); margin-bottom: 22px; }
  .bowls .item-name { font-weight: 600; font-size: 14px; }
  .bowls .item { margin-bottom: 18px; }
  .side-list { position: absolute; left: 410px; }
  .side-list .section-heading { margin-bottom: 22px; }
  .side-list .item-name { text-align: left; margin-bottom: 17px; }
  .dessert { top: 838px; }
  .soup { top: 1012px; }
</style>
</head>
<body>
<div class="canvas">
  <div class="menu-card"></div>

  <div class="brand">
    <span class="brand-dot"></span>
    <span class="brand-name">Maple Sprowt</span>
  </div>
  <h1 class="menu-title">MENU</h1>

  <section class="column salads">
    <h2 class="section-heading">Salads</h2>
    <div class="item"><p class="item-name">Brussel Sprout Ceasar</p><p class="item-desc">little gem romaine, toasted torn bread,<br>parmigiano reggiano</p></div>
    <div class="item"><p class="item-name">Heirloom Beet salad</p><p class="item-desc">shaved chioggia beet, roasted golden beet, red quinoa,<br>little gem, arugula, lemon vinaigrette</p></div>
    <div class="item"><p class="item-name">Zesty Black Bean &amp; Corn Salad<br>in lettuce cups</p><p class="item-desc">Black beans, avocado and roasted corn topped with<br>feta crumbles in butter lettuce</p></div>
    <div class="item"><p class="item-name">Green, red and white</p><p class="item-desc">Spring leaves, cherry tomatoes, avocado,<br>roasted almond and goat cheese</p></div>
  </section>

  <div class="column-divider"></div>

  <section class="column burgers">
    <h2 class="section-heading">Burgers, Wraps &amp; Sandwiches</h2>
    <div class="item"><p class="item-name">Sweet Potato, black bean veggie burgers<br>with cabbage - pepita slaw</p></div>
    <div class="item"><p class="item-name">Roasted Sprout, Arugula &amp; Hummus Wraps</p></div>
    <div class="item"><p class="item-name">Garden Burger</p></div>
    <div class="item has-desc"><p class="item-name">Beans &amp; Greens Quesadillas</p><p class="item-desc">Greens, Mexican cheese, beans and avocado, with salsa</p></div>
    <div class="item"><p class="item-name">Grilled vegetable &amp; mozzarella wrap</p></div>
    <div class="item"><p class="item-name">Sprout Burrito</p><p class="item-desc">Greens, Mexican cheese, beans, brown rice, roasted chili corn<br>and avocado, with ancho chili salsa, wheat tortilla</p></div>
  </section>

  <div class="rule rule-top"></div>
  <h2 class="section-heading toasts-heading">Toasts</h2>
  <div class="toast toast-a"><p class="item-name">Tomato &amp; Beet Bruschetta</p></div>
  <div class="toast toast-b"><p class="item-name">Everything Avocado</p><p class="item-desc">avocado on whole grain toast with our<br>signature spice blend</p></div>
  <div class="toast toast-c"><p class="item-name">Vegetable Melt on garlic</p></div>
  <div class="rule rule-bottom"></div>

  <section class="bowls">
    <h2 class="section-heading">Bowls</h2>
    <div class="item"><p class="item-name">Roasted vegetable,<br>&amp; spinach bowl</p></div>
    <div class="item"><p class="item-name">Sugar Snap Pea &amp; Carrot<br>Soba Noodles</p></div>
    <div class="item"><p class="item-name">Whole grain &amp; vegetable<br>buddha bowl</p></div>
    <div class="item"><p class="item-name">Orange &amp; Pistacio Quinoa</p></div>
  </section>

  <section class="side-list dessert">
    <h2 class="section-heading">Dessert</h2>
    <p class="item-name">Strawberry Balsamic Ice Cream sundae</p>
    <p class="item-name">Exotic fruit bowl</p>
    <p class="item-name">White and dark oatmeal cookie</p>
  </section>

  <section class="side-list soup">
    <h2 class="section-heading">Soup</h2>
    <p class="item-name">Black Bean Chowder</p>
  </section>
</div>
</body>
</html>
```